Harborlight Willow Home Care Business Cards

We are looking to create double sided, sleek business cards for our new Home Health Care Agency, Harborlight Willow Home Care, located in NJ. We want to appear established, professional and at the same time, stand out with a creative and original flair. It should have a luxurious, exclusive feel to it.
The theme colors from our logo should be incorporated into the project.

Our Logo is attached.

Information to be included on the business cards:

Insert Phone Icon: (555)-204-7390
Insert Website Icon: hwhcpx.example
Insert E-mail Icon: info@hwhcpx.example

Follow us on Social Media!
Insert Facebook Icon: (I will provide the link at a later time)
Insert Instagram Icon (I will provide the link at a later time)

In regard to location, we service the areas of: Bayville
Beachwood
Brick
Deal
Howell
Island Heights
Jackson
Lakehurst
Lakewood
Manchester Township
Point Pleasant Beach
Roosevelt
Long Branch
Toms River

All all it's neighboring areas.

However, that can take up a lot of room...therefore, I had in mind to use the backside of the card to have a MAP with all these areas marked on there...in addition to listing these service locations below the map.

We want the card to appear lively and vibrant.

Please note: I will provide the potential winner with the contact's name later on in the process.

A sample idea is attached below as well.

Use your creative juices!

Good luck!

• A map of our service areas on the back of the double sided card.
Sleek design
Our logo (refer to attachment below)

```html
<!DOCTYPE html>
<html lang="en">
<head>
<meta charset="utf-8">
<title>Harborlight Willow Home Care — Business Cards</title>
<link href="https://fonts.googleapis.com/css2?family=Montserrat:wght@700&family=Roboto:wght@400;500&display=swap" rel="stylesheet">
<style>
  :root {
    --page: #eef1f5;
    --card-top: #0d5fb8;
    --card-bottom: #0a3f86;
    --brand-blue: #1656a8;
    --leaf-green: #7ac143;
    --white: #ffffff;
  }
  * { box-sizing: border-box; margin: 0; padding: 0; }
  html, body { width: 1200px; height: 834px; overflow: hidden; }
  body {
    background: var(--page);
    font-family: "Roboto", Arial, sans-serif;
    position: relative;
  }
  .card {
    position: absolute;
    width: 520px;
    height: 298px;
    border-radius: 4px;
    background: linear-gradient(160deg, var(--card-top), var(--card-bottom));
    color: var(--white);
    box-shadow: 0 10px 28px rgba(10, 40, 90, 0.25);
  }
  .card-front { left: 50px; top: 90px; }
  .card-back { left: 630px; top: 90px; }

  .brand-name {
    font-family: "Montserrat", Arial, sans-serif;
    font-weight: 700;
    letter-spacing: 0.5px;
    line-height: 1.2;
  }

  /* front */
  .front-lockup { position: absolute; top: 58px; left: 0; right: 0; text-align: center; }
  .front-lockup .mark {
    display: block; width: 46px; height: 46px; margin: 0 auto 16px;
    border-radius: 50%; background: var(--leaf-green);
  }
  .front-lockup .brand-name { font-size: 21px; color: var(--white); white-space: nowrap; }
  .service-areas {
    position: absolute; left: 34px; right: 34px; bottom: 40px;
    list-style: none; display: flex; flex-wrap: wrap; justify-content: center;
    gap: 5px 14px; font-size: 12px;
  }
  .service-areas li::before {
    content: ""; display: inline-block; width: 6px; height: 6px; border-radius: 50%;
    background: var(--leaf-green); margin-right: 5px; vertical-align: middle;
  }

  /* back */
  .back-lockup { position: absolute; left: 28px; top: 104px; width: 200px; text-align: center; }
  .back-lockup .mark { display: block; width: 34px; height: 34px; border-radius: 50%; background: var(--leaf-green); margin: 0 auto 12px; }
  .back-lockup .brand-name { font-size: 14px; }
  .divider { position: absolute; left: 248px; top: 70px; width: 2px; height: 158px; background: var(--white); opacity: 0.85; }
  .contact-list { position: absolute; left: 276px; top: 82px; list-style: none; }
  .contact-list li { display: flex; align-items: center; gap: 10px; font-size: 19px; margin-bottom: 9px; white-space: nowrap; }
  .contact-list svg { width: 20px; height: 20px; flex: none; }
  .social-square { width: 20px; height: 20px; border-radius: 3px; background: var(--leaf-green); flex: none; }

  /* standalone lockup */
  .logo-lockup { position: absolute; left: 50px; top: 500px; width: 520px; text-align: center; }
  .logo-lockup .mark { display: block; width: 120px; height: 120px; border-radius: 50%; background: var(--brand-blue); margin: 0 auto 24px; }
  .logo-lockup .brand-name { font-size: 24px; color: var(--brand-blue); white-space: nowrap; }
</style>
</head>
<body>

<section class="card card-front" aria-label="Card front">
  <div class="front-lockup">
    <span class="mark"></span>
    <div class="brand-name">HARBORLIGHT WILLOW HOME CARE</div>
  </div>
  <ul class="service-areas">
    <li>Beachwood</li><li>Brick</li><li>Deal</li><li>Howell</li><li>Island Heights</li><li>Jackson</li>
    <li>Lakehurst</li><li>Lakewood</li><li>Manchester Township</li><li>Point Pleasant Beach</li>
    <li>Roosevelt</li><li>Long Branch</li><li>Toms River</li>
  </ul>
</section>

<section class="card card-back" aria-label="Card back">
  <div class="back-lockup">
    <span class="mark"></span>
    <div class="brand-name">HARBORLIGHT WILLOW HOME CARE</div>
  </div>
  <div class="divider"></div>
  <ul class="contact-list">
    <li>
      <svg viewBox="0 0 20 20"><rect width="20" height="20" rx="3" fill="#7ac143"/><path d="M6 4l3 3-1.5 1.5a8 8 0 0 0 4 4L13 11l3 3-2 2C9 16 4 11 4 6z" fill="#fff"/></svg>
      (555)-204-7390
    </li>
    <li>
      <svg viewBox="0 0 20 20"><rect width="20" height="20" rx="3" fill="#7ac143"/><rect x="4" y="6" width="12" height="8" fill="none" stroke="#fff" stroke-width="1.5"/><path d="M4 6l6 5 6-5" fill="none" stroke="#fff" stroke-width="1.5"/></svg>
      info@hwhcpx.example
    </li>
    <li>
      <svg viewBox="0 0 20 20"><circle cx="10" cy="10" r="9" fill="#7ac143"/><circle cx="10" cy="10" r="6" fill="none" stroke="#fff" stroke-width="1.3"/><path d="M4 10h12M10 4c-3 3-3 9 0 12M10 4c3 3 3 9 0 12" fill="none" stroke="#fff" stroke-width="1.1"/></svg>
      www.hwhcpx.example
    </li>
    <li>
      <span class="social-square"></span>
      @hwhcpx
    </li>
  </ul>
</section>

<section class="logo-lockup" aria-label="Logo">
  <span class="mark"></span>
  <div class="brand-name">HARBORLIGHT WILLOW HOME CARE</div>
</section>

</body>
</html>
```